Party Invitation for Newly Weds

We would like a A5 flyer-style invite in a file suitable for both hard-copy print and web-publishing. It should be designed in the style of a 1950's American Diner Menu incorporating the colours: Ivory, Crimson, Black, and possibly period Green.

We think using the shape of a 50's Juke Box could be a good platform for the design although we are very open to other ideas. We require the design to include the following features:

1. A tattoo-style heart with scroll banner containing our names - TED & CLARA

2. Main Heading - "Wedlock Wing-Ding & Nuptial Knees Up"

3. Feature Headings with icons - DRINK (with cocktail glasses), DANCE (with twisting silhouettes), DEVOUR (with burger & fries)

4. Sub Headings as Menu Items with descriptions as follows:

a. Hey Cat, When's It At?
Venue Doors @ 7pm
Bride & Groom Arrive @ 7.30pm
Be there or be sQuare!

b. Where To Go, Daddy-O!
The Millbrook
7, Fernley Street
Leeds, LS9 2QT

c. What's Cookin', Man?
DJs & Dancing all night from 7pm
Food Served on the terrace from 8pm
Late Bar from til 2am

d. Ya need digs? Dig this...
Special Rate for Party Guests at Marlow Grandstay
£79 Bed & Breakfast
Limited Numbers - Book Early
Call (0113) 5827364 and quote 'PEVOR'

e. If You Want To Share Your Good Vibes...
Your presence, your love and your laughter will be a real neat-o gift for us to cherish, but should you want to splash the cash and spread your love we would be MADE UP with a small donation towards our American Road Trip Honeymoon!!

f. Please R.S.V.P by July 1st.

g. Strictly Over 18's Only

Colors
87cfc6
f04b51
fefdec
1b1b1b

Requirements
Must have
• see project description
• genuine late 50's/early 60's retro style
• classic fonts
Nice to have
• asymmetric shapes
• personal touches
Should not have
• over dependence on food imagery - this is a menu-style design, not an actual menu!

```html
<!DOCTYPE html>
<html lang="en">
<head>
<meta charset="utf-8">
<title>Wedlock Wing-Ding &amp; Nuptial Knees Up – Ted &amp; Clara</title>
<link rel="stylesheet" href="https://fonts.googleapis.com/css2?family=Lobster&family=Almendra:wght@400;700&family=Dancing+Script:wght@700&display=swap">
<style>
  :root {
    --paper: #efe6d2;
    --teal: #87cfc6;
    --teal-deep: #5fbfae;
    --teal-floor: #4a9f8f;
    --crimson: #e0263f;
    --coral: #f04b51;
    --ivory: #fefdec;
    --peach: #fbd9bd;
    --peach-light: #fde8d4;
    --ink: #1b1b1b;
    --heart: #c8202c;
  }
  * { margin: 0; padding: 0; box-sizing: border-box; }
  html, body { width: 846px; height: 1200px; overflow: hidden; background: var(--paper); }
  .invite { position: relative; width: 846px; height: 1200px; background: var(--paper); }
  .invite__shapes { position: absolute; inset: 0; }
  .abs { position: absolute; }

  .sparkles { position: absolute; border-radius: 8px; background: radial-gradient(circle, rgba(254,253,236,.35), rgba(135,207,198,0) 70%); }
  .sparkles--left { left: 24px; top: 24px; width: 150px; height: 290px; }
  .sparkles--right { left: 672px; top: 24px; width: 150px; height: 290px; }

  .floor { top: 928px; height: 256px; background: linear-gradient(135deg, var(--ink), #4a4540 50%, var(--ink)); }
  .floor--left { left: 16px; width: 104px; }
  .floor--right { left: 726px; width: 104px; }

  .heart-art { left: 250px; top: 92px; width: 330px; height: 280px;
    background: radial-gradient(ellipse at 50% 45%, var(--heart) 0 44%, rgba(200,32,44,0) 62%); }
  .names-banner { left: 300px; top: 238px; width: 246px; height: 46px; background: var(--teal-deep);
    border: 2px solid var(--ink); transform: rotate(4deg); display: flex; align-items: center; justify-content: center;
    font-family: "Dancing Script", cursive; font-size: 27px; color: var(--ink); }

  .title { left: 184px; top: 372px; width: 480px; text-align: center; font-family: "Lobster", cursive;
    color: var(--peach-light); font-size: 43px; line-height: 44px;
    text-shadow: 2px 2px 0 var(--ink), -1px -1px 0 var(--ink), 1px -1px 0 var(--ink), -1px 1px 0 var(--ink); }

  .feature { font-family: "Lobster", cursive; font-size: 25px; color: var(--ink); transform: rotate(-14deg); letter-spacing: 1px; }
  .icon { border-radius: 6px; }
  .icon--drink { left: 188px; top: 494px; width: 34px; height: 66px; background: linear-gradient(#e46a5a, #c9c2b8); }
  .icon--dance { left: 328px; top: 490px; width: 58px; height: 74px; background: linear-gradient(#2e2e2e, #e38a8f); }
  .icon--devour { left: 492px; top: 500px; width: 70px; height: 56px; background: linear-gradient(#f4b233, #c7452c); }

  .menu-item h2 { font-family: "Lobster", cursive; font-weight: 400; font-size: 24px; line-height: 27px; color: var(--ink); }
  .menu-item p { font-family: "Almendra", serif; font-size: 20px; line-height: 24px; color: var(--ink); }
  .menu-item p.small { font-size: 15px; line-height: 19px; }
  .notes { left: 176px; top: 950px; font-family: "Almendra", serif; font-weight: 700; font-size: 15px; line-height: 25px; color: var(--crimson); list-style: none; }
  .notes li::before { content: ""; display: inline-block; width: 6px; height: 6px; border: 1.5px solid var(--teal-floor); border-radius: 50%; margin-right: 6px; vertical-align: middle; }

  .vibes-title { left: 92px; top: 1032px; width: 664px; text-align: center; font-family: "Lobster", cursive;
    font-weight: 400; font-size: 23px; line-height: 34px; color: var(--peach-light); }
  .vibes-text { left: 100px; top: 1070px; width: 646px; text-align: center; font-family: "Almendra", serif;
    font-size: 17px; line-height: 18px; color: var(--ivory); }
</style>
</head>
<body>
<div class="invite">
  <svg class="invite__shapes" width="846" height="1200" viewBox="0 0 846 1200" aria-hidden="true">
    <defs>
      <linearGradient id="skyFade" x1="0" y1="0" x2="0" y2="1">
        <stop offset="0" stop-color="#94d6cd"/><stop offset="1" stop-color="#6ec3b5"/>
      </linearGradient>
    </defs>
    <rect x="16" y="16" width="814" height="1168" fill="url(#skyFade)"/>
    <polygon points="16,900 150,888 150,928 16,928" fill="var(--teal-floor)"/>
    <polygon points="830,900 700,888 700,928 830,928" fill="var(--teal-floor)"/>
    <rect x="16" y="928" width="814" height="256" fill="var(--ink)"/>

    <!-- jukebox body -->
    <path d="M104,1030 V398 A319,319 0 0 1 742,398 V1030 Z" fill="var(--ink)"/>
    <path d="M120,1026 V398 A303,303 0 0 1 726,398 V1026 Z" fill="var(--coral)"/>
    <path d="M150,1026 V398 A273,273 0 0 1 696,398 V1026 Z" fill="var(--ink)"/>
    <path d="M156,1026 V398 A267,267 0 0 1 690,398 V1026 Z" fill="var(--crimson)"/>
    <path d="M180,470 V398 A243,243 0 0 1 666,398 V470 Z" fill="var(--ink)"/>
    <path d="M184,470 V398 A239,239 0 0 1 662,398 V470 Z" fill="var(--peach)"/>
    <polygon points="326,46 530,46 512,116 344,116" fill="var(--crimson)" stroke="var(--ink)" stroke-width="3"/>

    <!-- title band -->
    <rect x="44" y="364" width="764" height="60" rx="30" fill="var(--coral)" stroke="var(--ink)" stroke-width="3"/>
    <rect x="44" y="420" width="764" height="52" rx="26" fill="var(--coral)" stroke="var(--ink)" stroke-width="3"/>
    <line x1="70" y1="392" x2="180" y2="392" stroke="var(--ink)" stroke-width="2"/>
    <line x1="666" y1="392" x2="780" y2="392" stroke="var(--ink)" stroke-width="2"/>
    <line x1="70" y1="446" x2="180" y2="446" stroke="var(--ink)" stroke-width="2"/>
    <line x1="666" y1="446" x2="780" y2="446" stroke="var(--ink)" stroke-width="2"/>
    <rect x="180" y="366" width="486" height="106" rx="10" fill="var(--crimson)" stroke="var(--ink)" stroke-width="3"/>
    <circle cx="194" cy="418" r="8" fill="var(--peach-light)" stroke="var(--ink)" stroke-width="2"/>
    <circle cx="652" cy="418" r="8" fill="var(--peach-light)" stroke="var(--ink)" stroke-width="2"/>

    <!-- menu panel -->
    <rect x="156" y="474" width="534" height="552" fill="var(--ink)"/>
    <rect x="160" y="476" width="526" height="550" fill="var(--peach-light)"/>
    <line x1="182" y1="586" x2="392" y2="586" stroke="var(--crimson)" stroke-width="3"/>
    <circle cx="392" cy="586" r="4" fill="var(--crimson)"/><circle cx="182" cy="586" r="4" fill="var(--crimson)"/>
    <line x1="456" y1="586" x2="666" y2="586" stroke="var(--crimson)" stroke-width="3"/>
    <circle cx="456" cy="586" r="4" fill="var(--crimson)"/><circle cx="666" cy="586" r="4" fill="var(--crimson)"/>
    <line x1="424" y1="586" x2="424" y2="994" stroke="var(--crimson)" stroke-width="3"/>
    <circle cx="424" cy="586" r="4" fill="var(--crimson)"/><circle cx="424" cy="994" r="4" fill="var(--crimson)"/>

    <!-- base ribbons -->
    <rect x="40" y="1100" width="766" height="50" rx="25" fill="var(--crimson)" stroke="var(--ink)" stroke-width="3"/>
    <rect x="68" y="1066" width="712" height="40" rx="20" fill="var(--crimson)" stroke="var(--ink)" stroke-width="3"/>
    <rect x="92" y="1030" width="664" height="38" rx="19" fill="var(--crimson)" stroke="var(--ink)" stroke-width="3"/>
    <rect x="100" y="1064" width="646" height="80" fill="var(--crimson)"/>
  </svg>

  <div class="sparkles sparkles--left" role="img" aria-label="Four-point retro sparkle stars"></div>
  <div class="sparkles sparkles--right" role="img" aria-label="Four-point retro sparkle stars"></div>
  <div class="abs floor floor--left" role="img" aria-label="Black and ivory checkerboard diner floor"></div>
  <div class="abs floor floor--right" role="img" aria-label="Black and ivory checkerboard diner floor"></div>

  <div class="abs heart-art" role="img" aria-label="Tattoo-style red heart pierced by an arrow"></div>
  <div class="abs names-banner">Ted &amp; Clara</div>

  <h1 class="abs title">Wedlock Wing-Ding<br>&amp; Nuptial Knees Up</h1>

  <div class="abs icon icon--drink" role="img" aria-label="Cocktail glass"></div>
  <div class="abs feature" style="left:230px;top:512px;">DRINK</div>
  <div class="abs icon icon--dance" role="img" aria-label="Couple twisting on the dance floor"></div>
  <div class="abs feature" style="left:396px;top:518px;">DANCE</div>
  <div class="abs icon icon--devour" role="img" aria-label="Burger and fries"></div>
  <div class="abs feature" style="left:562px;top:512px;">DEVOUR</div>

  <section class="abs menu-item" style="left:186px;top:600px;width:232px;">
    <h2>Hey Cat,<br>When's It At?</h2>
    <p>Venue Doors @ 7pm<br>Bride &amp; Groom Arrive<br>@ 7.30pm<br>Be there or be sQuare!</p>
  </section>
  <section class="abs menu-item" style="left:186px;top:776px;width:232px;">
    <h2>Where To Go,<br>Daddy-O!</h2>
    <p style="line-height:27px;">The Millbrook<br>7, Fernley Street<br>Leeds, LS9 2QT</p>
  </section>
  <ul class="abs notes">
    <li>Please R.S.V.P by July 1st.</li>
    <li>Strictly Over 18's Only</li>
  </ul>

  <section class="abs menu-item" style="left:452px;top:600px;width:230px;">
    <h2>What's Cookin',<br>Man?</h2>
    <p style="line-height:21px;">DJs &amp; Dancing<br>all night from 7pm.<br>Food Served on the<br>terrace from 8pm.<br>Late Bar from til 2am</p>
  </section>
  <section class="abs menu-item" style="left:452px;top:776px;width:230px;">
    <h2>Ya need digs?<br>&nbsp;&nbsp;Dig this…</h2>
    <p style="line-height:26px;">Special Rate for Party<br>Guests at<br>Marlow Grandstay<br>£79 Bed &amp; Breakfast</p>
    <p class="small">Limited Numbers - Book Early<br>Call (0113) 5827364<br>and quote 'PEVOR'</p>
  </section>

  <h2 class="abs vibes-title">If You Want To Share Your Good Vibes…</h2>
  <p class="abs vibes-text">Your presence, your love and your laughter will be a real<br>neat-o gift for us to cherish, but should you want to splash<br>the cash and spread your love we would be MADE UP with<br>a small donation towards our American Road Trip Honeymoon!!</p>
</div>
</body>
</html>
```